Hairdressing Salon called; Velvet Tress. Style Lives Here

Velvet Tress
We Love Hair
418 Penrose Lane Birch Vale
5183742
Business card not to fussy.
I would like it to be a Black background with White and/or Grey lettering.

I really like the business card attached, so if the front looked like this I would be really happy, but would also like my address and phone number on the front.

On the back I would like two options of
1: reward card; buy any Haircare product over $20 on any visit and on the tenth product receive a complimentry Treatment and
2: appointment times and date

Industry/Entity Type

Business

Contact Information for Business Card

Velvet Tress
We Love Hair
5183742
418 Penrose Lane, Birch Vale
This must all be included on the front of the card

Font styles to use
Serif
Decorative
Script

Colors
1b1b1b
757575
ffffff

Requirements
Must have
• My phone number and address
Should not have
• Pictures on the front

```html
<!DOCTYPE html>
<html lang="en">
<head>
<meta charset="utf-8">
<title>Velvet Tress – Reward Card</title>
<link href="https://fonts.googleapis.com/css2?family=Cinzel:wght@600&display=swap" rel="stylesheet">
<style>
  :root {
    --ink-black: #1b1b1b;
    --panel-black: #141515;
    --edge-grey: #2c2f2f;
    --mid-grey: #757575;
    --stamp-white: #ffffff;
  }
  html, body {
    margin: 0;
    padding: 0;
    width: 1200px;
    height: 698px;
    overflow: hidden;
    background: var(--ink-black);
  }
  .reward-card {
    position: relative;
    width: 1200px;
    height: 698px;
    overflow: hidden;
    background: var(--ink-black);
  }
  .side-band {
    position: absolute;
    top: 0;
    height: 698px;
  }
  .side-band--left {
    left: 0;
    width: 310px;
    background: linear-gradient(90deg, #1e2020 0%, #232626 60%, #2a2d2d 100%);
  }
  .side-band--right {
    left: 890px;
    width: 310px;
    background: linear-gradient(90deg, #2f3333 0%, #262929 45%, #1c1e1e 100%);
  }
  .stamp-panel {
    position: absolute;
    left: 310px;
    top: 0;
    width: 580px;
    height: 698px;
    background: radial-gradient(ellipse at 50% 50%, #1d1f1f 0%, var(--panel-black) 70%, #101111 100%);
  }
  .stamp-grid {
    position: absolute;
    left: 0;
    top: 0;
  }
  .stamp-spot {
    fill: var(--stamp-white);
  }
  .reward-terms {
    position: absolute;
    left: -145px;
    top: 269px;
    width: 600px;
    height: 160px;
    transform: rotate(-90deg);
    transform-origin: 50% 50%;
    margin: 0;
    display: flex;
    flex-direction: column;
    justify-content: center;
    text-align: center;
    font-family: "Cinzel", "Times New Roman", serif;
    font-weight: 600;
    font-size: 27px;
    line-height: 38px;
    letter-spacing: 0.5px;
    color: var(--stamp-white);
  }
  .reward-terms span {
    display: block;
    white-space: nowrap;
  }
</style>
</head>
<body>
  <main class="reward-card">
    <div class="side-band side-band--left" role="img" aria-label="Faint dark damask ornament pattern"></div>
    <div class="stamp-panel" role="img" aria-label="Faint dark damask ornament pattern behind the stamp spots"></div>
    <div class="side-band side-band--right" role="img" aria-label="Faint dark damask ornament pattern"></div>

    <svg class="stamp-grid" width="1200" height="698" viewBox="0 0 1200 698" aria-label="Ten reward stamp spots">
      <circle class="stamp-spot" cx="411" cy="132" r="72"/>
      <circle class="stamp-spot" cx="602" cy="132" r="72"/>
      <circle class="stamp-spot" cx="793" cy="132" r="72"/>
      <circle class="stamp-spot" cx="411" cy="340" r="72"/>
      <circle class="stamp-spot" cx="602" cy="340" r="72"/>
      <circle class="stamp-spot" cx="793" cy="340" r="72"/>
      <circle class="stamp-spot" cx="984" cy="340" r="72"/>
      <circle class="stamp-spot" cx="411" cy="548" r="72"/>
      <circle class="stamp-spot" cx="602" cy="548" r="72"/>
      <circle class="stamp-spot" cx="793" cy="548" r="72"/>
    </svg>

    <p class="reward-terms">
      <span>buy any Haircare product</span>
      <span>over $20 on any visit</span>
      <span>and on the tenth product</span>
      <span>receive a complimentry Treatment</span>
    </p>
  </main>
</body>
</html>
```